A new fitness program IRON FORGE 8X needs to create a new mini-mag

We need the following word doc turned into a similar look and feel to our other programs (also attached). Images will be provided. It doesn't need to be over complex, but needs to keep the high quality and standards of our other booklets that focuses on male fitness and health.
The design includes creating the cover as well using a similar format to the example provided.

```html
<!DOCTYPE html>
<html lang="en">
<head>
<meta charset="utf-8">
<title>Iron Forge 8X – 28 Day Primer Training Program</title>
<link href="https://fonts.googleapis.com/css2?family=Ultra&family=Roboto+Slab:wght@300;400&family=Oswald:wght@500;700&family=Arimo:wght@400;700&display=swap" rel="stylesheet">
<style>
:root{
  --bg:#efefef;
  --page:#ffffff;
  --ink:#1d1d1d;
  --grey:#3b3b3b;
  --red:#e3202b;
  --green:#3ea64b;
  --row-a:#cfe6c1;
  --row-b:#e3f0da;
  --note:#a9d293;
  --maroon:#6e1230;
}
*{box-sizing:border-box;margin:0;padding:0}
html,body{width:934px;height:1200px;overflow:hidden}
body{background:var(--bg);position:relative;font-family:'Arimo',sans-serif;color:var(--ink)}
.page{position:absolute;width:442px;height:570px;background:var(--page);box-shadow:0 1px 6px rgba(0,0,0,.25);overflow:hidden;padding:0 30px}
.page--1{left:18px;top:18px}
.page--2{left:474px;top:18px}
.page--3{left:18px;top:606px}
.page--4{left:474px;top:606px}
.photo{position:absolute;z-index:0}
.photo--p2{right:0;top:300px;width:140px;height:270px;background:linear-gradient(90deg,rgba(255,255,255,0),rgba(226,210,200,.55))}
.photo--p3{right:0;top:0;width:130px;height:570px;background:linear-gradient(90deg,rgba(255,255,255,0),rgba(232,220,210,.6))}
.page>*:not(.photo){position:relative;z-index:1}
.masthead{text-align:center;padding-top:16px;height:102px;white-space:nowrap}
.masthead__title{font-family:'Ultra',serif;font-weight:400;font-size:38px;line-height:44px;height:44px;color:var(--ink);letter-spacing:.5px}
.masthead__sub{font-family:'Roboto Slab',serif;font-weight:300;font-size:34px;line-height:40px;height:40px;color:var(--grey);letter-spacing:1px}
.day{font-family:'Oswald',sans-serif;font-weight:700;font-size:18px;line-height:24px;height:24px;color:var(--red);text-align:center;margin:10px 0 5px;letter-spacing:.3px;white-space:nowrap}
.plan{width:100%;table-layout:fixed;border-collapse:separate;border-spacing:0 1px;font-size:8.5px}
.plan th{background:var(--green);color:#fff;font-weight:700;height:19px;line-height:19px;text-align:center;white-space:nowrap}
.plan td{height:20px;line-height:12px;text-align:center;background:var(--row-a);white-space:nowrap;overflow:hidden}
.plan tr:nth-child(even) td{background:var(--row-b)}
.plan td:first-child{text-align:left;padding-left:6px}
.plan td.section{font-family:'Oswald',sans-serif;font-weight:500;font-size:14px;line-height:20px;height:21px;background:var(--row-b)!important;text-align:center;padding-left:0}
.plan td.gap{height:19px;background:var(--row-b)!important}
.plan col.c1{width:53%}.plan col.c2{width:10%}.plan col.c3{width:13%}.plan col.c4{width:24%}
.guide{background:var(--note);font-size:7.5px;line-height:9.5px;padding:5px 8px 6px;margin-top:-1px}
.guide ul{list-style:square;padding-left:22px}
.remark{font-size:7.8px;line-height:10px;margin-top:10px;padding-right:4px}
.remark__title{font-family:'Oswald',sans-serif;font-weight:700;font-style:italic;color:var(--red);font-size:11px;line-height:14px;text-decoration:underline;margin-bottom:6px}
.remark p{margin-bottom:7px}
.remark b{font-weight:700}
.remark .link{color:var(--red);font-weight:700}
.url-bar{position:absolute;left:100px;top:528px;width:250px;height:26px;background:var(--maroon);border-radius:4px;color:#fff;font-family:'Oswald',sans-serif;font-weight:700;font-size:16px;line-height:26px;text-align:center;letter-spacing:.5px;white-space:nowrap}
.clock{position:absolute;left:348px;top:476px;width:82px;height:88px;border-radius:12px;background:radial-gradient(circle at 50% 55%,#f4f4f4 0 34%,#b8123a 36% 60%,#8d0e2c 62%)}
</style>
</head>
<body>

<section class="page page--1">
  <header class="masthead">
    <h1 class="masthead__title">28 DAY "PRIMER"</h1>
    <p class="masthead__sub">TRAINING PROGRAM</p>
  </header>
  <h2 class="day">DAY 1: CHEST &amp; BACK</h2>
  <table class="plan">
    <colgroup><col class="c1"><col class="c2"><col class="c3"><col class="c4"></colgroup>
    <tr><th>EXERCISE</th><th>SETS</th><th>REPS</th><th>REST (SECONDS)</th></tr>
    <tr><td>A: Barbell bench press</td><td>3</td><td>8-10</td><td>60</td></tr>
    <tr><td>B: Seated cable row</td><td>3</td><td>10-12</td><td>60</td></tr>
    <tr><td>C: Incline dumbbell press</td><td>3</td><td>8-10</td><td>60</td></tr>
    <tr><td>D: One arm dumbbell row</td><td>3</td><td>10-12</td><td>60</td></tr>
    <tr><td>E: Decline dumbbell press</td><td>3</td><td>15</td><td>60</td></tr>
    <tr><td>F: Barbell deadlift</td><td>3</td><td>15</td><td>60</td></tr>
  </table>
  <h2 class="day">DAY 2: ARMS</h2>
  <table class="plan">
    <colgroup><col class="c1"><col class="c2"><col class="c3"><col class="c4"></colgroup>
    <tr><th>EXERCISE</th><th>SETS</th><th>REPS</th><th>REST (SECONDS)</th></tr>
    <tr><td class="section" colspan="4">BICEPS</td></tr>
    <tr><td>A: Single arm cable curls</td><td>3</td><td>15</td><td>0 (alt each arm)</td></tr>
    <tr><td>B: Standing single arm Hammer curls</td><td>3</td><td>8-10</td><td>60</td></tr>
    <tr><td>C: Seated double arm incline DB curls</td><td>3</td><td>10-12</td><td>60</td></tr>
    <tr><td class="gap" colspan="4"></td></tr>
    <tr><td class="section" colspan="4">TRICEPS</td></tr>
    <tr><td>A: Straight bar tricep pushdown</td><td>3</td><td>15</td><td>60</td></tr>
    <tr><td>B: Close grip benchpress</td><td>3</td><td>8-10</td><td>60</td></tr>
    <tr><td>C: Dips</td><td>3</td><td>FAILURE</td><td>45</td></tr>
  </table>
</section>

<section class="page page--2">
  <div class="photo photo--p2" role="img" aria-label="Photo of a smiling woman training, faded into the page edge"></div>
  <header class="masthead">
    <h1 class="masthead__title">28 DAY "PRIMER"</h1>
    <p class="masthead__sub">TRAINING PROGRAM</p>
  </header>
  <h2 class="day">DAY 3: HiiT &amp; ABS</h2>
  <table class="plan">
    <colgroup><col class="c1"><col class="c2"><col class="c3"><col class="c4"></colgroup>
    <tr><th>EXERCISE</th><th>SETS</th><th>REPS</th><th>REST (SECONDS)</th></tr>
    <tr><td class="section" colspan="4">ABS</td></tr>
    <tr><td>A: Plank</td><td>2</td><td>1 min</td><td>45</td></tr>
    <tr><td>B: Weighted crunches</td><td>2</td><td>10</td><td>45</td></tr>
    <tr><td>C: Mountain climbers</td><td>2</td><td>15</td><td>45</td></tr>
    <tr><td>D: Bicycle crunch</td><td>2</td><td>15</td><td>45</td></tr>
    <tr><td>E: Plank</td><td>1</td><td>FAILURE</td><td>-</td></tr>
  </table>
  <div class="guide">
    Perform a minimum of 25min HiiT or intense training activity. (See our HiiT guide)<br>
    We recommend starting with:
    <ul><li>5 min W/UP</li><li>30sec high intensity followed by 45sec low intensity (recovery)</li><li>Repeat for 15min</li><li>5min C/DOWN</li></ul>
  </div>
  <h2 class="day">DAY 4: ARMS</h2>
  <table class="plan">
    <colgroup><col class="c1"><col class="c2"><col class="c3"><col class="c4"></colgroup>
    <tr><th>EXERCISE</th><th>SETS</th><th>REPS</th><th>REST (SECONDS)</th></tr>
    <tr><td class="section" colspan="4">LEGS</td></tr>
    <tr><td>A: Squat</td><td>4</td><td>10-12</td><td>60</td></tr>
    <tr><td>B: Leg extension</td><td>4</td><td>12-15</td><td>60</td></tr>
    <tr><td>C: Leg curls</td><td>4</td><td>8</td><td>60</td></tr>
    <tr><td>D: Stiff legged deadlift</td><td>4</td><td>12-15</td><td>60</td></tr>
    <tr><td>E: Calf raises (Seated or standing)</td><td>4</td><td>15-20</td><td>45</td></tr>
  </table>
</section>

<section class="page page--3">
  <div class="photo photo--p3" role="img" aria-label="Photo of a woman's face, faded into the page edge"></div>
  <h2 class="day" style="margin-top:16px">DAY 5: HiiT &amp; ABS</h2>
  <table class="plan">
    <colgroup><col class="c1"><col class="c2"><col class="c3"><col class="c4"></colgroup>
    <tr><th>EXERCISE</th><th>SETS</th><th>REPS</th><th>REST (SECONDS)</th></tr>
    <tr><td class="section" colspan="4">ABS</td></tr>
    <tr><td>A: Plank</td><td>2</td><td>1 min</td><td>45</td></tr>
    <tr><td>B: Weighted crunches</td><td>2</td><td>10</td><td>45</td></tr>
    <tr><td>C: Mountain climbers</td><td>2</td><td>15</td><td>45</td></tr>
    <tr><td>D: Bicycle crunch</td><td>2</td><td>15</td><td>45</td></tr>
    <tr><td>E: Plank</td><td>1</td><td>FAILURE</td><td>-</td></tr>
  </table>
  <div class="guide">
    Perform a minimum of 25min HiiT or intense training activity. (See our HiiT guide)<br>
    We recommend starting with:
    <ul><li>5 min W/UP</li><li>30sec high intensity followed by 45sec low intensity (recovery)</li><li>Repeat for 15min</li><li>5min C/DOWN</li></ul>
  </div>
  <h2 class="day" style="margin-top:22px">DAY 6: SHOULDERS &amp; LATS</h2>
  <table class="plan">
    <colgroup><col class="c1"><col class="c2"><col class="c3"><col class="c4"></colgroup>
    <tr><th>EXERCISE</th><th>SETS</th><th>REPS</th><th>REST (SECONDS)</th></tr>
    <tr><td class="section" colspan="4">SHOULDERS</td></tr>
    <tr><td>A: Seated dumbbell shoulder press</td><td>3</td><td>12-15</td><td>60</td></tr>
    <tr><td>B: Rear delt pulls (Using rope on cable machine)</td><td>3</td><td>10-12</td><td>60</td></tr>
    <tr><td>C: Side lateral raises</td><td>3</td><td>10-12</td><td>60</td></tr>
    <tr><td class="gap" colspan="4"></td></tr>
    <tr><td class="section" colspan="4">LATS</td></tr>
    <tr><td>A: Wide grip lat pulldown</td><td>3</td><td>8-10</td><td>60</td></tr>
    <tr><td>B: V-bar pull-up (concentrate on lats not arms!)</td><td>3</td><td>FAILURE</td><td>60</td></tr>
    <tr><td>C: Standing late rope cable pull down</td><td>3</td><td>12-15</td><td>45</td></tr>
  </table>
</section>

<section class="page page--4">
  <header class="masthead">
    <h1 class="masthead__title">28 DAY "PRIMER"</h1>
    <p class="masthead__sub">TRAINING PROGRAM</p>
  </header>
  <h2 class="day">DAY 7: SSC &amp; ABS</h2>
  <table class="plan">
    <colgroup><col class="c1"><col class="c2"><col class="c3"><col class="c4"></colgroup>
    <tr><th>EXERCISE</th><th>SETS</th><th>REPS</th><th>REST (SECONDS)</th></tr>
    <tr><td class="section" colspan="4">ABS</td></tr>
    <tr><td>A: Plank</td><td>2</td><td>1 min</td><td>45</td></tr>
    <tr><td>B: Weighted crunches</td><td>2</td><td>10</td><td>45</td></tr>
    <tr><td>D: Mountain climbers</td><td>2</td><td>15</td><td>45</td></tr>
    <tr><td>D: Bicycle crunch</td><td>2</td><td>15</td><td>45</td></tr>
    <tr><td>F: Plank</td><td>1</td><td>FAILURE</td><td>-</td></tr>
  </table>
  <div class="guide">
    This is your active recovery day that has been created to motivate you and help your body recover from the previous week. Use it to your advantage! SSC – Steady State Cardio (recovery)
    <ul>
      <li>A minimum of 45min of a fast paced walk/jog/bike ride</li>
      <li>Preferable first thing in the morning on an empty stomach if possible</li>
      <li>Reflect on the week that was, think over what worked and what didn't</li>
      <li>Prepare your mind and body for the week ahead and how you will improve</li>
      <li>Stay positive, focused &amp; most of all, make sure you're enjoying it!</li>
    </ul>
  </div>
  <div class="remark">
    <p class="remark__title">NOTE:</p>
    <p>This 28 DAY PRIMER program is intended for use as a lead-in program for our full <b>IRON FORGE 8X PROGRAM.</b></p>
    <p>If you'd like access to the full <b>IRON FORGE 8X PROGRAM</b> then head to <span class="link">www.ironforge8x.com</span> for details.</p>
    <p>If at anytime you have questions or concerns, please contact us: <b>coach@ironforge8x.com</b></p>
  </div>
  <div class="url-bar">WWW.IRONFORGE8X.COM</div>
  <div class="clock" role="img" aria-label="Illustration of a red alarm clock"></div>
</section>

</body>
</html>
```